Harbor Learning Center Posters Showing Building Blocks

We need poster designs for a School in Arizona for kids with Autism. There will be 4 such posters needed which highlight our schools building blocks. Requirements for all 4 posters are as followed: 1) We need the Harbor Learning Center Logo on each poster. I have included attachment. 2) The posters need the following titles: Building Block #1 (for the first poster), Building Block #2 for the 2nd poster, Building Block #3 for the 3rd poster, and Building Block #4 for the forth poster. 3) The main text and focus of the posters will be the following key words: For the first poster the words "Kids first in every decision". The words for the second poster are: "Students are friends with each other, and welcome new students with open arms." The words for the 3rd poster are: "The school is quiet, and students are working hard to do their best." The words for the 4th poster are: "Parents see amazing improvement in their child." 4) We would love to use some of the kids art from our schools if possible. Use your expertise to decide. I will send these out as well. 5) Try and design the posters around the key words from each poster 6) I am sure if landscape or portrait would be best so I will let the experts decide. All 4 posters need to be the same layout once decided.

Target Market(s)

These posters are for the school only. Prospective students/parents will see these posters so they will be used for Marketing from that perspective. We may put out into local community in future.

Industry/Entity Type

School

Font styles to use
Serif

Requirements
Must have
• 1) Logo (Harbor Learning Center for Growth and Discovery)
• 2) Title: as described in write up
• 3) Key words: as described in write up
Nice to have
• Kids art from school. Note: This is the first time that I have been on this site so I may have made a mistake by putting 4 posters on one project. I am assuming that I would need to pay more to have 4 posters so let me know if I need to modify the project in any way?

```html
<!DOCTYPE html>
<html lang="en">
<head>
<meta charset="utf-8">
<title>Harbor Learning Center – Building Block Posters</title>
<link rel="stylesheet" href="https://fonts.googleapis.com/css2?family=Alfa+Slab+One&family=Archivo+Black&family=Oswald:wght@500;600;700&family=Playfair+Display:ital,wght@0,400;0,700;1,400;1,700&family=Roboto+Slab:wght@400;700&display=swap">
<style>
  :root {
    --page: #ffffff;
    --ink: #ffffff;
    --title-yellow: #f2e544;
    --block-1: #1b86a6;
    --block-2: #c2532f;
    --block-3: #7d7db5;
    --block-4: #3e7877;
    --frame-line: rgba(255,255,255,0.45);
    --rule-blue: #5ab4e0;
    --brand-square: #f2e544;
  }
  * { margin: 0; padding: 0; box-sizing: border-box; }
  html, body { width: 1000px; height: 1200px; overflow: hidden; background: var(--page); }
  .sheet { position: relative; width: 1000px; height: 1200px; }

  .poster {
    position: absolute; width: 352px; height: 545px; overflow: hidden;
    color: var(--ink);
    box-shadow: 0 4px 10px rgba(0,0,0,0.35);
  }
  .poster--1 { left: 112px; top: 28px;  background: var(--block-1); }
  .poster--2 { left: 536px; top: 28px;  background: var(--block-2); }
  .poster--3 { left: 112px; top: 622px; background: var(--block-3); }
  .poster--4 { left: 536px; top: 622px; background: var(--block-4); }

  .frame {
    position: absolute; left: 10px; right: 10px; top: 72px; bottom: -2px;
    border: 1px solid var(--frame-line); border-bottom: none;
  }

  .brand {
    position: absolute; left: 22px; top: 22px; width: 170px;
    display: flex; align-items: flex-start; gap: 6px;
  }
  .brand__mark { width: 14px; height: 14px; background: var(--brand-square); flex: none; margin-top: 2px; }
  .brand__name {
    font-family: "Roboto Slab", serif; font-weight: 400; font-size: 9px;
    line-height: 1.2; color: var(--ink);
  }

  .block-title {
    position: absolute; right: 20px; top: 22px; text-align: left;
    font-family: "Roboto Slab", serif; font-size: 18px; line-height: 1.25;
    color: var(--title-yellow);
  }

  .headline {
    position: absolute; left: 0; right: 0; z-index: 2; text-align: center;
    text-shadow: 0 2px 3px rgba(0,0,0,0.3);
  }
  .headline > div { line-height: 1; }

  .slab-heavy { font-family: "Alfa Slab One", serif; }
  .slab { font-family: "Roboto Slab", serif; }
  .condensed { font-family: "Oswald", sans-serif; font-weight: 700; }
  .serif { font-family: "Playfair Display", serif; }
  .italic { font-family: "Playfair Display", serif; font-style: italic; }
  .heavy { font-family: "Archivo Black", sans-serif; }

  .dotted-rule { width: 280px; margin: 0 auto; border-top: 3px dotted var(--ink); }

  .photo { position: absolute; z-index: 1; }
  .photo--1 { left: 11px; right: 0; top: 372px; height: 173px; background: linear-gradient(180deg, #5a4a4a 0%, #8a6a5e 55%, #e8e0d6 100%); }
  .photo--2 { left: 0; right: 0; top: 372px; height: 173px; background: linear-gradient(180deg, #e8c9a8 0%, #c98f72 50%, #d7b39a 100%); }
  .photo--3 { left: 0; right: 0; top: 392px; height: 153px; background: linear-gradient(180deg, #d9c5c0 0%, #a8a0c8 50%, #7b5a48 100%); }
  .photo--4 { left: 0; right: 0; top: 345px; height: 200px; background: linear-gradient(180deg, #e9dcc0 0%, #8a6670 50%, #ece7e0 100%); }
</style>
</head>
<body>
<main class="sheet">

  <section class="poster poster--1">
    <div class="frame"></div>
    <div class="brand"><span class="brand__mark"></span><span class="brand__name">Harbor Learning Center for Growth and Discovery</span></div>
    <div class="block-title">Building<br>Block #1</div>
    <div class="headline" style="top:100px">
      <div class="slab-heavy" style="font-size:54px">KIDS</div>
      <div class="slab-heavy" style="font-size:60px; margin-top:6px">FIRST</div>
      <div class="dotted-rule" style="margin-top:14px"></div>
      <div class="slab" style="font-size:40px; margin-top:8px">IN EVERY</div>
      <div class="dotted-rule" style="margin-top:10px"></div>
      <div class="slab" style="font-size:40px; font-weight:700; margin-top:8px">DECISION</div>
    </div>
    <div class="photo photo--1" role="img" aria-label="Photo of a boy writing at a desk beside a stack of books"></div>
  </section>

  <section class="poster poster--2">
    <div class="frame"></div>
    <div class="brand"><span class="brand__mark"></span><span class="brand__name">Harbor Learning Center for Growth and Discovery</span></div>
    <div class="block-title">Building<br>Block #2</div>
    <div class="headline" style="top:88px">
      <div class="condensed" style="font-size:54px">STUDENTS</div>
      <div class="italic" style="font-size:24px; margin-top:2px">are</div>
      <div class="serif" style="font-size:48px; margin-top:-2px">— friends —</div>
      <div class="italic" style="font-size:30px; margin-top:2px">with each other,</div>
      <div style="margin-top:4px"><span class="italic" style="font-size:24px">and</span> <span class="condensed" style="font-size:40px">WELCOME</span></div>
      <div class="heavy" style="font-size:29px; margin-top:2px">new students</div>
      <div><span class="italic" style="font-size:18px">with</span> <span class="heavy" style="font-size:29px">open arms</span></div>
    </div>
    <div class="photo photo--2" role="img" aria-label="Photo of a cheerful group of students together"></div>
  </section>

  <section class="poster poster--3">
    <div class="frame"></div>
    <div class="brand"><span class="brand__mark"></span><span class="brand__name">Harbor Learning Center for Growth and Discovery</span></div>
    <div class="block-title">Building<br>Block #3</div>
    <div class="headline" style="top:92px">
      <div class="italic" style="font-size:24px">The</div>
      <div class="condensed" style="font-size:56px">SCHOOL</div>
      <div style="display:flex; justify-content:center; align-items:center; gap:10px; margin-top:4px">
        <svg width="60" height="14" viewBox="0 0 60 14" aria-hidden="true"><g fill="rgba(255,255,255,0.5)"><polygon points="0,0 8,0 15,7 8,14 0,14 7,7"/><polygon points="15,0 23,0 30,7 23,14 15,14 22,7"/><polygon points="30,0 38,0 45,7 38,14 30,14 37,7"/></g></svg>
        <span><span class="italic" style="font-size:22px">is</span> <span class="serif" style="font-size:40px">quiet</span></span>
        <svg width="60" height="14" viewBox="0 0 60 14" aria-hidden="true"><g fill="rgba(255,255,255,0.5)"><polygon points="60,0 52,0 45,7 52,14 60,14 53,7"/><polygon points="45,0 37,0 30,7 37,14 45,14 38,7"/><polygon points="30,0 22,0 15,7 22,14 30,14 23,7"/></g></svg>
      </div>
      <div style="margin-top:8px"><span class="italic" style="font-size:22px">and</span> <span class="serif" style="font-size:42px">students</span></div>
      <div style="margin-top:10px"><span class="serif" style="font-size:22px">are</span> <span class="condensed" style="font-size:40px">working hard</span></div>
      <div style="margin-top:10px"><span class="italic" style="font-size:24px">to</span> <span class="heavy" style="font-size:30px">do</span> <span class="italic" style="font-size:26px">their</span> <span class="serif" style="font-size:36px">BEST.</span></div>
    </div>
    <div class="photo photo--3" role="img" aria-label="Photo of two children lying down reading books between stacks of books"></div>
  </section>

  <section class="poster poster--4">
    <div class="frame"></div>
    <div class="brand"><span class="brand__mark"></span><span class="brand__name">Harbor Learning Center for Growth and Discovery</span></div>
    <div class="block-title">Building<br>Block #4</div>
    <div class="headline" style="top:92px">
      <div style="display:flex; justify-content:center; align-items:center; gap:10px">
        <span style="color:var(--rule-blue); font-size:14px; letter-spacing:2px">***</span>
        <span class="condensed" style="font-size:50px">PARENTS</span>
        <span style="color:var(--rule-blue); font-size:14px; letter-spacing:2px">***</span>
      </div>
      <div class="heavy" style="font-size:30px; margin-top:4px">see amazing</div>
      <div class="condensed" style="font-size:44px; margin-top:4px">improvement</div>
      <div style="display:flex; justify-content:center; align-items:center; gap:10px; margin-top:4px">
        <span style="width:70px; border-top:2px solid var(--rule-blue)"></span>
        <span class="italic" style="font-size:20px">in their</span>
        <span style="width:70px; border-top:2px solid var(--rule-blue)"></span>
      </div>
      <div class="serif" style="font-size:46px; line-height:1.05">child.</div>
    </div>
    <div class="photo photo--4" role="img" aria-label="Photo of a mother helping her smiling son with homework"></div>
  </section>

</main>
</body>
</html>
```